Business Card Design

I need Business card designs with following on cards:

Dalton Mewse
Director

M: +61 491 268 304
D: +61 7 5590 1826
F: +61 7 5590 6071
E: dalton@torvelgroup.com.au

Torvel Group
Suite 4/58 North Calloway Road
Corvale Heads QLD 4299

Rex Halloran
Director

M: +61 438 952 107
D: +61 7 5590 1826
F: +61 7 5590 6071
E: rex@torvelgroup.com.au

Torvel Group
Corvale Heads QLD 4299

Torvel Group Logo has been attached to brief.

```html
<!DOCTYPE html>
<html lang="en">
<head>
<meta charset="utf-8">
<title>Torvel Group – Business Card</title>
<link rel="stylesheet" href="https://fonts.googleapis.com/css2?family=Arimo:wght@400;700&display=swap">
<style>
  :root {
    --brand-red: #d7081e;
    --ink: #231f20;
    --paper: #ffffff;
  }
  html, body {
    margin: 0;
    padding: 0;
    width: 1200px;
    height: 739px;
    overflow: hidden;
    background: var(--paper);
  }
  .card {
    position: relative;
    width: 1200px;
    height: 739px;
    background: var(--paper);
    font-family: "Arimo", Arial, sans-serif;
    color: var(--ink);
    overflow: hidden;
  }
  .card__swoosh {
    position: absolute;
    left: 0;
    top: 0;
    width: 1200px;
    height: 739px;
  }
  .swoosh-red { fill: var(--brand-red); }
  .swoosh-dark { fill: var(--ink); }

  .brand-name {
    position: absolute;
    left: 0;
    right: 0;
    top: 188px;
    margin: 0;
    text-align: center;
    font-size: 100px;
    font-weight: 700;
    letter-spacing: -1px;
    color: var(--ink);
    line-height: 1;
  }
  .brand-address {
    position: absolute;
    left: 0;
    right: 0;
    top: 335px;
    margin: 0;
    text-align: center;
    font-size: 23px;
    font-weight: 700;
    letter-spacing: 0.6px;
    color: var(--ink);
  }
  .brand-address .accent { color: var(--brand-red); }
  .brand-address .divider { margin: 0 6px; }

  .contact {
    position: absolute;
    left: 322px;
    top: 446px;
  }
  .contact__name {
    margin: 0;
    font-size: 41px;
    font-weight: 700;
    color: var(--brand-red);
    letter-spacing: 0.5px;
    line-height: 1.2;
  }
  .contact__role {
    font-size: 25px;
    color: var(--ink);
    margin-left: 6px;
    letter-spacing: 0.3px;
  }
  .contact__list {
    list-style: none;
    margin: 10px 0 0 4px;
    padding: 0;
    font-size: 28px;
    font-weight: 700;
    line-height: 33.5px;
    letter-spacing: 0.4px;
    color: var(--ink);
  }
</style>
</head>
<body>
  <main class="card">
    <svg class="card__swoosh" viewBox="0 0 1200 739" aria-hidden="true">
      <path class="swoosh-red" d="M0,590 Q420,705 770,690 Q1010,680 1200,598 L1200,739 L0,739 Z"/>
      <path class="swoosh-dark" d="M720,688 Q1010,655 1200,533 L1200,598 Q1010,680 720,688 Z"/>
    </svg>

    <h1 class="brand-name">Torvel Group</h1>

    <p class="brand-address">
      <span class="accent">Torvel Group</span><span class="divider">I</span>Suite 4/58 North Calloway Road<span class="divider">I</span><span class="accent">Corvale Heads QLD 4299</span>
    </p>

    <section class="contact">
      <h2 class="contact__name">Rex Halloran <span class="contact__role">(DIRECTOR)</span></h2>
      <ul class="contact__list">
        <li>M: +61 438 952 107</li>
        <li>D: +61 7 5590 1826</li>
        <li>F: +61 7 5590 6071</li>
        <li>E: rex@torvelgroup.com.au</li>
      </ul>
    </section>
  </main>
</body>
</html>
```